Photography Business, Business Card

Looking for a unique cutting edge card that takes advantage of the latest printing technologies. Please review this site for all the options they office: https://plumeprints.example. If you can think it they can do it. And if you have an idea and do not know if they can do it, I will check into it.
Updates

Target Market(s)

People and places I took images of and future clients.

Industry/Entity Type

Photography

Contact Information for Business Card

Name, cell & email. Colin Hartley, chartley@kvnphoto.example, 318-742-9061

Colors

Designer to choose only greyscale colors for use in the design.

Requirements
Must have
• 100% cutting edge. Is so great, those I hand it to always show it to someone else. A piece of art.
Nice to have
• Blacks, silvers, greys, some red. Maybe other colors?

```html
<!DOCTYPE html>
<html lang="en">
<head>
<meta charset="UTF-8">
<title>KVN Photo Business Card</title>
<link href="https://fonts.googleapis.com/css2?family=Questrial&family=Mrs+Saint+Delafield&display=swap" rel="stylesheet">
<style>
  :root {
    --page: #fefefe;
    --border: #ffffff;
    --charcoal: #262626;
    --charcoal-edge: #1c1c1c;
    --graphite: #353535;
    --silver: #d4d4d4;
    --accent-red: #ed1c24;
    --ink: #ffffff;
  }
  * { margin: 0; padding: 0; box-sizing: border-box; }
  html, body { width: 1200px; height: 951px; overflow: hidden; background: var(--page); }
  body { position: relative; font-family: "Questrial", "Century Gothic", sans-serif; }

  .card {
    position: absolute;
    width: 521px;
    height: 304px;
    background: var(--border);
    padding: 8px;
    box-shadow: 0 4px 22px rgba(0, 0, 0, 0.10);
  }
  .card--front { left: 339px; top: 120px; }
  .card--back { left: 353px; top: 537px; }

  .card__face {
    position: relative;
    width: 100%;
    height: 100%;
    background: radial-gradient(ellipse at center, var(--charcoal) 0%, var(--charcoal-edge) 100%);
    overflow: hidden;
    color: var(--ink);
  }

  .lens-circle {
    position: absolute;
    width: 344px;
    height: 344px;
    left: 50%;
    top: 50%;
    transform: translate(-50%, -50%);
    border-radius: 50%;
    background: radial-gradient(circle at 50% 40%, #3d3d3d 0%, var(--graphite) 60%, #2e2e2e 100%);
    box-shadow: inset 0 0 12px rgba(0, 0, 0, 0.55), 0 0 8px rgba(0, 0, 0, 0.35);
  }

  .frame-corner {
    position: absolute;
    width: 62px;
    height: 62px;
    border-color: var(--accent-red);
    border-style: solid;
    border-width: 0;
  }
  .frame-corner--tl { left: 30px; top: 25px; border-top-width: 2px; border-left-width: 2px; }
  .frame-corner--tr { right: 30px; top: 25px; border-top-width: 2px; border-right-width: 2px; }
  .frame-corner--bl { left: 30px; bottom: 26px; border-bottom-width: 2px; border-left-width: 2px; }
  .frame-corner--br { right: 30px; bottom: 26px; border-bottom-width: 2px; border-right-width: 2px; }

  .brand-name {
    position: absolute;
    left: 0; right: 0;
    top: 50%;
    transform: translateY(-50%);
    text-align: center;
    font-size: 62px;
    letter-spacing: 10px;
    text-indent: 10px;
    line-height: 1;
    color: var(--ink);
  }

  .person-name {
    position: absolute;
    left: 0; right: 0;
    top: 110px;
    text-align: center;
    font-family: "Mrs Saint Delafield", cursive;
    font-size: 56px;
    line-height: 1;
    color: var(--ink);
  }

  .contact {
    position: absolute;
    left: 0; right: 0;
    top: 201px;
    text-align: center;
    font-size: 13px;
    line-height: 15px;
    color: var(--silver);
  }
</style>
</head>
<body>
  <section class="card card--front">
    <div class="card__face">
      <div class="lens-circle"></div>
      <span class="frame-corner frame-corner--tl"></span>
      <span class="frame-corner frame-corner--tr"></span>
      <span class="frame-corner frame-corner--bl"></span>
      <span class="frame-corner frame-corner--br"></span>
      <div class="brand-name">KVN</div>
    </div>
  </section>

  <section class="card card--back">
    <div class="card__face">
      <div class="lens-circle"></div>
      <span class="frame-corner frame-corner--tl"></span>
      <span class="frame-corner frame-corner--tr"></span>
      <span class="frame-corner frame-corner--bl"></span>
      <span class="frame-corner frame-corner--br"></span>
      <div class="person-name">Colin Hartley</div>
      <div class="contact">
        <p class="contact__phone">318-742-9061</p>
        <p class="contact__email">chartley@kvnphoto.example</p>
      </div>
    </div>
  </section>
</body>
</html>
```